A empresa queria:
" O Grupo VELQUAR busca a conversão das mais inovadoras tecnologias nas soluções mais impactantes para o mercado. Nesta perspectiva, a VELQUAR BIOTECNOLOGIA ANIMAL constitui nosso segmento encarregado por transformar o conhecimento científico em bioferramentas inteligentes que agreguem o máximo valor às biotecnologias da reprodução tornando-as cada vez mais produtivas e lucrativas. Atuamos há mais de 10 anos no contexto da Reprodução Animal, dentro e fora do Brasil, executando tanto biotecnologias tradicionais, como a IATF (Inseminação Artificial em Tempo Fixo) e a SOV/TE (Superovulação e Transferência de Embriões), quanto bioferramentas modernas e de altíssimo impacto como a produção de embriões FIV (Fecundados In Vitro) e a clonagem animal. Nossa missão é contribuir decisivamente para o aprimoramento e emprego cada vez mais eficiente, rentável e satisfatório das biotecnologias da reprodução. Estruturado em valores como integridade, excelência e trabalho em equipe, constituímos uma companhia altamente amigável e absolutamente confiável para a execução das biotecnologias mais modernas com vistas, sempre, à plena satisfação do cliente. "

```html
<!DOCTYPE html>
<html lang="pt-BR">
<head>
<meta charset="utf-8">
<title>VELQUAR — Reprodução Animal</title>
<link rel="stylesheet" href="https://fonts.googleapis.com/css2?family=Open+Sans:wght@400;600;700&display=swap">
<style>
:root{
  --green:#5aa43a;
  --green-dark:#3f8a2a;
  --green-light:#8cc63f;
  --ink:#444;
  --muted:#888;
  --line:#e3e3e3;
  --page:#ffffff;
  --outer:#f3f4f2;
  --teal:#3fbfae;
}
*{box-sizing:border-box;margin:0;padding:0}
html,body{width:1200px;height:1200px;overflow:hidden}
body{background:var(--outer);font-family:"Open Sans",Arial,sans-serif;color:var(--ink);position:relative}
.page{position:absolute;left:271px;top:0;width:658px;height:1200px;background:var(--page);box-shadow:0 0 12px rgba(0,0,0,.08)}
.abs{position:absolute}
.topbar{left:0;top:0;width:658px;height:14px;background:var(--green)}
.toplinks{right:16px;top:2px;font-size:7px;color:#fff;display:flex;gap:14px}
.brand{display:flex;align-items:center;gap:8px}
.header-brand{left:60px;top:45px}
.brand-mark{width:26px;height:26px;background:var(--green)}
.brand-name{font-size:24px;font-weight:600;color:var(--green);letter-spacing:.5px;line-height:1}
.mainnav{right:30px;top:36px;font-size:8px;font-weight:600;color:#666;display:flex;gap:12px;align-items:center}
.mainnav .social{width:14px;height:14px;background:var(--green)}
.tabs{left:252px;top:67px;display:flex;font-size:10px;color:#444}
.tab{padding:12px 14px;height:46px;line-height:1.2;white-space:nowrap}
.tab.active{border:1px solid var(--line);border-bottom:none;border-top:3px solid var(--green);background:#fff}
.tab.wide{padding-top:8px}
.navrule{left:0;top:112px;width:658px;height:1px;background:var(--line)}
.hero{left:17px;top:132px;width:624px;height:247px;background:linear-gradient(180deg,#6fae3c 0%,#8fc14f 45%,#5f9a30 100%)}
.swoosh{left:0;top:360px;width:658px;height:200px}
.section-title{font-size:15px;font-weight:400;color:#444;padding-left:10px;border-left:3px solid var(--green);line-height:18px}
.intro-title{left:65px;top:418px}
.intro-text{left:65px;top:452px;width:280px;font-size:8.5px;line-height:14px;color:var(--muted)}
.video{left:365px;top:408px;width:221px;height:173px;border:3px solid #fff;box-shadow:0 0 5px rgba(0,0,0,.25);background:linear-gradient(135deg,#c9c4b6,#8a9a6a 60%,#5d7a3a)}
.play{left:95px;top:70px}
.divider{left:17px;top:612px;width:624px;height:1px;background:var(--line)}
.news-title{left:62px;top:641px}
.projects-title{left:382px;top:641px}
.news-card{left:58px;width:269px}
.news-head{background:var(--green);color:#fff;padding:6px 10px;height:46px}
.news-head h3{font-size:12px;font-weight:600;line-height:16px}
.news-head span{font-size:7px;opacity:.85}
.news-body{font-size:8px;line-height:12px;color:var(--muted);padding:10px 2px 0}
.more{font-size:6.5px;color:var(--green-dark);font-weight:700;margin-top:8px;display:block}
.btn{left:177px;top:1013px;width:84px;height:24px;border:1px solid #ccc;border-radius:12px;font-size:7px;text-align:center;line-height:22px;color:#666}
.grid{left:370px;top:684px;width:213px;display:grid;grid-template-columns:repeat(3,67px);gap:6px 6px}
.thumb{height:50px}
.t1{background:linear-gradient(#9bc3d6,#6c8f3b)}
.t2{background:linear-gradient(#d8ccb0,#a88d5d)}
.t3{background:linear-gradient(#bcd4e4,#8fa35f)}
.t4{background:linear-gradient(#8aa8c0,#3e5d7a)}
.t5{background:linear-gradient(#cfd6dc,#7c8a96)}
.t6{background:linear-gradient(#e2e7ee,#a2aebf)}
.t7{background:linear-gradient(#d0c8b8,#6f675a)}
.t8{background:linear-gradient(#606a78,#2c3340)}
.t9{background:linear-gradient(#e8e8e8,#b9b9b9)}
.dots{left:462px;top:853px;display:flex;gap:5px}
.dots i{width:7px;height:7px;border-radius:50%;border:1px solid var(--green);display:block}
.dots i.on{background:var(--green)}
.banner{left:370px;top:893px;width:213px;height:134px;background:linear-gradient(135deg,#7fe0cf,var(--teal) 55%,#2a9c8c);color:#fff}
.banner-text{left:12px;top:80px;font-size:19px;font-weight:700;line-height:20px}
.banner-sub{right:12px;bottom:6px;font-size:7px}
.chev{right:14px;top:10px}
.foot-rule{left:0;top:1056px;width:658px;height:1px;background:var(--line)}
.foot-brand{left:62px;top:1104px;gap:6px}
.foot-brand .brand-mark{width:20px;height:20px}
.foot-brand .brand-name{font-size:19px}
.foot-links{left:200px;top:1086px;font-size:8px;line-height:13px;color:#555;list-style:none}
.foot-contact{left:400px;top:1119px;font-size:7.5px;color:#555;display:flex;gap:12px;align-items:center}
.foot-contact .social{width:14px;height:14px;background:#444}
.bottombar{left:0;top:1176px;width:658px;height:24px;background:var(--green);color:#fff;font-size:6.5px;text-align:center;line-height:24px}
</style>
</head>
<body>
<div class="page">
  <div class="abs topbar">
    <div class="abs toplinks"><span>contato@velquar.com</span><span>(00) 0000-482-915</span><span>EN</span></div>
  </div>

  <div class="abs brand header-brand"><span class="brand-mark"></span><span class="brand-name">VELQUAR</span></div>

  <nav class="abs mainnav"><span>EMPRESA</span><span>SERVIÇOS ▾</span><span>CONTATO</span><span class="social"></span></nav>

  <div class="abs tabs">
    <div class="tab active">Reprodução Animal</div>
    <div class="tab">Diagnósticos</div>
    <div class="tab wide">Animais<br>Geneticamente Modificados</div>
  </div>
  <div class="abs navrule"></div>

  <div class="abs hero" role="img" aria-label="Fotografia de uma ovelha deitada na grama verde"></div>

  <svg class="abs swoosh" viewBox="0 0 658 200" aria-hidden="true">
    <path d="M380 80 C500 40 600 30 658 60 L658 200 C610 120 520 90 380 80Z" fill="#e6f2dc"/>
    <path d="M420 70 C520 40 610 40 658 70" stroke="#cfe6bd" stroke-width="2" fill="none"/>
  </svg>

  <h2 class="abs section-title intro-title">Reprodução Animal</h2>
  <p class="abs intro-text">Lorem ipsum dolor sit amet, consectetur adipiscing elit, sed do eiusmod tempor incididunt ut labore et dolore magna aliqua. Ut enim ad minim veniam, quis nostrud exercitation ullamco laboris nisi ut aliquip ex ea commodo consequat. Duis aute irure dolor in reprehenderit in voluptate velit esse cillum dolore eu fugiat nulla pariatur. Excepteur sint occaecat cupidatat non proident, sunt in culpa qui officia deserunt mollit anim id est laborum.</p>

  <div class="abs video" role="img" aria-label="Vídeo com ovelhas no pasto">
    <svg class="abs play" width="32" height="32" viewBox="0 0 32 32" aria-hidden="true">
      <circle cx="16" cy="16" r="15" fill="rgba(255,255,255,.85)"/>
      <path d="M13 10 L23 16 L13 22Z" fill="#555"/>
    </svg>
  </div>

  <div class="abs divider"></div>

  <h2 class="abs section-title news-title">Notícias</h2>
  <h2 class="abs section-title projects-title">Projetos</h2>

  <article class="abs news-card" style="top:684px">
    <div class="news-head"><h3>Lorem ipsum dolor sit amet</h3><span>15 de março de 2014</span></div>
    <p class="news-body">Duis aute irure dolor in reprehenderit in voluptate velit esse cillum dolore eu fugiat nulla pariatur. Excepteur sint occaecat cupidatat non proident, sunt in culpa qui officia deserunt mollit anim id est laborum.<span class="more">SAIBA MAIS ›</span></p>
  </article>

  <article class="abs news-card" style="top:847px">
    <div class="news-head"><h3>Lorem ipsum dolor sit amet</h3><span>02 de março de 2014</span></div>
    <p class="news-body">Duis aute irure dolor in reprehenderit in voluptate velit esse cillum dolore eu fugiat nulla pariatur. Excepteur sint occaecat cupidatat non proident, sunt in culpa qui officia deserunt mollit anim id est laborum.<span class="more">SAIBA MAIS ›</span></p>
  </article>

  <div class="abs btn">VER MAIS</div>

  <div class="abs grid">
    <div class="thumb t1" role="img" aria-label="Foto de bovinos"></div>
    <div class="thumb t2" role="img" aria-label="Foto de cão"></div>
    <div class="thumb t3" role="img" aria-label="Foto de ovelha"></div>
    <div class="thumb t4" role="img" aria-label="Foto de laboratório"></div>
    <div class="thumb t5" role="img" aria-label="Foto de equipamento de pesquisa"></div>
    <div class="thumb t6" role="img" aria-label="Foto de seringas"></div>
    <div class="thumb t7" role="img" aria-label="Foto de registros médicos"></div>
    <div class="thumb t8" role="img" aria-label="Foto de técnico no laboratório"></div>
    <div class="thumb t9" role="img" aria-label="Foto de célula ao microscópio"></div>
  </div>
  <div class="abs dots"><i class="on"></i><i></i><i></i></div>

  <div class="abs banner" role="img" aria-label="Banner de mapeamento genético">
    <svg class="abs chev" width="40" height="36" viewBox="0 0 40 36" aria-hidden="true">
      <path d="M4 4 L18 18 L4 32 M20 4 L34 18 L20 32" stroke="#fff" stroke-width="5" fill="none"/>
    </svg>
    <div class="abs banner-text">MAPEAMENTO<br>GENÉTICO</div>
    <div class="abs banner-sub">Saiba mais</div>
  </div>

  <div class="abs foot-rule"></div>
  <div class="abs brand foot-brand"><span class="brand-mark"></span><span class="brand-name">VELQUAR</span></div>
  <ul class="abs foot-links">
    <li>Nossa Empresa</li>
    <li>Reprodução Animal</li>
    <li>Diagnósticos</li>
    <li>Animais<br>Geneticamente Modificados</li>
  </ul>
  <div class="abs foot-contact"><span class="social"></span><span>contato@velquar.com</span><span>(00) 0000-482-915</span><span>EN</span></div>

  <div class="abs bottombar">© 2014 - VELQUAR BIOTECNOLOGIA</div>
</div>
</body>
</html>
```